Business Card design for shipping company 'FERNHOLT INTERNATIONAL LTD'

Classic / traditional business card in black Garamond / Times New Roman or similar text for a shipping / marine transport company, containing the following information:

QUOTE

FERNHOLT INTERNATIONAL LTD

MARTIN QUESTEDGE FICS

T: +44 7902 615370
E: cargo@fernholt-example.com

UNQUOTE

Target Market(s)

Marine / Shipping industry

Contact Information for Business Card

FERNHOLT INTERNATIONAL LTD MARTIN QUESTEDGE FICS T: +44 7902 615370 E: cargo@fernholt-example.com

Font styles to use
Serif

Colors

Designer to choose colors to be used in the design.

Requirements
Must have
• Garamond / Times New Roman or similar text in black colour

```html
<!DOCTYPE html>
<html lang="en">
<head>
<meta charset="utf-8">
<title>Fernholt International Ltd — Business Card</title>
<link href="https://fonts.googleapis.com/css2?family=EB+Garamond:wght@500;600&display=swap" rel="stylesheet">
<style>
  :root {
    --backdrop: #262626;
    --card: #0b0b0c;
    --accent: #2ea3dc;
    --ink-light: #f2f2f2;
    --rule: #cfcfcf;
  }
  * { box-sizing: border-box; margin: 0; padding: 0; }
  html, body { width: 1200px; height: 904px; overflow: hidden; }
  body {
    background: var(--backdrop);
    font-family: "EB Garamond", "Times New Roman", serif;
    position: relative;
  }
  .card {
    position: absolute;
    left: 310px;
    width: 580px;
    height: 332px;
    background: var(--card);
    border-radius: 3px;
    box-shadow: 0 14px 30px rgba(0,0,0,0.55);
  }
  .card--front { top: 86px; }
  .card--back { top: 486px; }

  .wordmark {
    color: var(--accent);
    font-weight: 600;
    letter-spacing: 0.04em;
    line-height: 1.05;
    text-align: center;
  }
  .card--front .wordmark {
    position: absolute;
    left: 0; right: 0; top: 120px;
    font-size: 36px;
  }
  .card--front .wordmark .wordmark__sub { font-size: 21px; }

  .card--back .wordmark {
    position: absolute;
    right: 38px; top: 44px;
    width: 270px;
    font-size: 26px;
  }
  .card--back .wordmark .wordmark__sub { font-size: 15px; }
  .wordmark__sub { display: block; letter-spacing: 0.08em; }

  .rule { position: absolute; height: 1px; background: var(--rule); }
  .rule--top { left: 230px; right: 38px; top: 142px; }
  .rule--bottom { left: 44px; width: 300px; top: 258px; }

  .contact {
    position: absolute;
    display: flex; align-items: center; gap: 10px;
    color: var(--ink-light);
    font-size: 21px;
    font-weight: 500;
  }
  .contact svg { width: 18px; height: 18px; fill: var(--accent); flex: none; }
  .contact--email { right: 38px; top: 154px; }
  .contact--phone { left: 44px; top: 270px; }

  .holder {
    position: absolute;
    left: 44px; top: 218px;
    color: var(--accent);
    font-size: 23px;
    font-weight: 600;
    letter-spacing: 0.03em;
  }
</style>
</head>
<body>
  <section class="card card--front" aria-label="Card front">
    <div class="wordmark">FERNHOLT<span class="wordmark__sub">INTERNATIONAL LTD</span></div>
  </section>

  <section class="card card--back" aria-label="Card back">
    <div class="wordmark">FERNHOLT<span class="wordmark__sub">INTERNATIONAL LTD</span></div>
    <div class="rule rule--top"></div>
    <div class="contact contact--email">
      <svg viewBox="0 0 20 20" aria-hidden="true"><path d="M1 4h18v12H1z M2 5l8 6 8-6" fill="none" stroke="#2ea3dc" stroke-width="0"/><path d="M1 4h18v1.5L10 11 1 5.5z"/><path d="M1 7.2l9 5.6 9-5.6V16H1z"/></svg>
      <span>cargo@fernholt-example.com</span>
    </div>
    <div class="holder">MARTIN QUESTEDGE FICS</div>
    <div class="rule rule--bottom"></div>
    <div class="contact contact--phone">
      <svg viewBox="0 0 20 20" aria-hidden="true"><path d="M2 7c0-3 3-4 8-4s8 1 8 4l-3 1-1-2H6L5 8z"/><path d="M5 9h10l2 7H3z M10 11a2 2 0 1 0 0.01 0z"/></svg>
      <span>+44 7902 615370</span>
    </div>
  </section>
</body>
</html>
```